Hearthway Homes website creation

A slick professional landing page it needs to be a very engaging custom designed landing page.

It must have a lead generation tool/box similar to my competitors that will recognise the address when they start to enter the address or postcode.

My main competitors websites to use ideas from to build trust and look correct are: www.brindlemarsh.com quorvahomes.com

Target Market(s)

People looking to sell their house or property fast. We will buy their property

Industry/Entity Type

Real Estate

Coding

Coded - Design and coding required

Number of Pages Required

1 page

Requirements
Must have
• A lead generation tool that is similar to my competitors to gather their essential details. (please check www.quorvahomes.com or www.brindlemarsh.com to see what i want.

It also must have all the aspects my competitors has on their landing page. All companies in this industry have this on the landing page. These include: Logos to build trust. Ours can be The Vellmoor Logo, the seen on TV logo, The Harrowgate Ledger online logo. Also we need a step by step process map to show the customer how it works.

If the customer is about to leave the page it Must have flash ups that ask the customer to fill in 4 boxes. first name, surname, email, Phone number and address. Check out quorvahomes.com to see what i want.

must have a comparison table similar to my competitors. I can include this on the draft.

Must have my frequently asked questions for google SEO ( I will upload these to here to the winner to add this page at the end.

It must be a slick professional design that tells people they are dealing with a company they can trust who has the funds on hand to purchase hundreds of property.
Nice to have
• It must be a slick professional design that tells people they are dealing with a company they can trust who has the funds on hand to purchase hundreds of property.
Should not have
• Anything cheap or tacky looking.

```html
<!DOCTYPE html>
<html lang="en">
<head>
<meta charset="utf-8">
<title>Hearthway Homes – Sell Your House Fast</title>
<link rel="stylesheet" href="https://fonts.googleapis.com/css2?family=Roboto:wght@400;500;700&family=Tinos&display=swap">
<style>
  :root {
    --brand-blue: #6797f8;
    --nav-blue: #6998f8;
    --phone-blue: #5d8ef7;
    --ink: #333740;
    --hero-start: rgba(92, 108, 214, 0.92);
    --hero-mid: rgba(118, 96, 214, 0.9);
    --hero-end: #8a47c9;
    --white: #ffffff;
  }
  * { box-sizing: border-box; margin: 0; padding: 0; }
  html, body {
    width: 1200px; height: 1200px; overflow: hidden;
    background: var(--white);
    font-family: "Roboto", Arial, sans-serif;
  }
  .page { position: relative; width: 1200px; height: 1200px; }

  .call-now {
    position: absolute; left: 138px; top: 240px;
    display: flex; align-items: center; gap: 14px;
    color: var(--phone-blue);
    font-family: "Tinos", "Times New Roman", serif;
    font-size: 22px;
  }
  .call-now svg { width: 44px; height: 58px; }
  .call-now span { margin-top: 20px; }

  .brand {
    position: absolute; left: 522px; top: 250px;
    display: flex; align-items: center; gap: 10px;
    font-size: 22px; font-weight: 500; color: var(--ink);
  }
  .brand-mark { width: 16px; height: 16px; background: var(--brand-blue); }

  .cta-top {
    position: absolute; left: 876px; top: 260px;
    width: 168px; height: 42px;
    background: var(--brand-blue); color: var(--white);
    border-radius: 6px;
    display: flex; align-items: center; justify-content: center;
    font-size: 20px;
  }

  .main-nav {
    position: absolute; left: 36px; top: 327px;
    width: 1136px; height: 60px;
    background: var(--nav-blue);
    display: flex; align-items: center; justify-content: space-around;
    padding: 0 30px;
  }
  .main-nav a { color: var(--white); text-decoration: none; font-size: 14px; }

  .hero {
    position: absolute; left: 36px; top: 387px;
    width: 1136px; height: 364px; overflow: hidden;
  }
  .hero-photo {
    position: absolute; inset: 0;
    background: linear-gradient(90deg, #8f86b4 0%, #7c7ec6 35%, #7a70cf 55%, transparent 70%), var(--hero-end);
  }
  .hero-overlay {
    position: absolute; inset: 0;
    background: linear-gradient(100deg, var(--hero-start) 0%, var(--hero-mid) 55%, var(--hero-end) 100%);
    opacity: 0.85;
  }
  .hero-title {
    position: absolute; left: 420px; top: 32px;
    color: var(--white); font-size: 29px; font-weight: 700;
  }
  .benefits {
    position: absolute; left: 721px; top: 90px;
    list-style: none; color: var(--white);
    font-size: 15px; font-weight: 700;
  }
  .benefits li { display: flex; align-items: center; gap: 14px; height: 24px; }
  .benefits li + li { margin-top: 20px; }
  .benefits svg { width: 22px; height: 18px; }
  .hero-btn {
    position: absolute; left: 721px;
    width: 194px; height: 47px;
    border: 2px solid var(--white); border-radius: 6px;
    color: var(--white); font-size: 15px; font-weight: 700;
    display: flex; align-items: center; justify-content: center;
    padding-bottom: 8px;
  }
  .hero-btn.offer { top: 222px; }
  .hero-btn.postcode { top: 296px; }

  .process-title {
    position: absolute; left: 370px; top: 788px;
    color: var(--brand-blue); font-size: 29px; font-weight: 400;
  }
</style>
</head>
<body>
<div class="page">
  <div class="call-now">
    <svg viewBox="0 0 44 58" aria-hidden="true">
      <rect x="6" y="3" width="30" height="50" rx="5" transform="rotate(-12 21 28)" fill="none" stroke="var(--phone-blue)" stroke-width="4"/>
      <circle cx="27" cy="46" r="2.5" fill="var(--phone-blue)"/>
    </svg>
    <span>Call Now Free 01632960418</span>
  </div>

  <div class="brand">
    <span class="brand-mark"></span>
    <span>Hearthway Homes</span>
  </div>

  <div class="cta-top">Get a Cash Offer</div>

  <nav class="main-nav">
    <a href="#">How It Works |</a>
    <a href="#">Sell House Fast |</a>
    <a href="#">Cash House Buyers |</a>
    <a href="#">Value My House |</a>
    <a href="#">More Services |</a>
    <a href="#">About Us |</a>
  </nav>

  <section class="hero">
    <div class="hero-photo" role="img" aria-label="Photo of a couple at home looking at a laptop together"></div>
    <div class="hero-overlay"></div>
    <h1 class="hero-title">We can buy any house in a time that suits you.</h1>
    <ul class="benefits">
      <li><svg viewBox="0 0 22 18" aria-hidden="true"><path d="M2 9l6 6L20 3" fill="none" stroke="#fff" stroke-width="4"/></svg>FREE cash offer</li>
      <li><svg viewBox="0 0 22 18" aria-hidden="true"><path d="M2 9l6 6L20 3" fill="none" stroke="#fff" stroke-width="4"/></svg>No estate agent or solicitor fees</li>
      <li><svg viewBox="0 0 22 18" aria-hidden="true"><path d="M2 9l6 6L20 3" fill="none" stroke="#fff" stroke-width="4"/></svg>A GUARANTEED sale for any property</li>
    </ul>
    <div class="hero-btn offer">Get a Cash Offer</div>
    <div class="hero-btn postcode">Enter Your Postcode</div>
  </section>

  <h2 class="process-title">The process is simple...</h2>
</div>
</body>
</html>
```